Business card and stationary for ATM Company
Fun modern design for new quirky company
Business card and stationary for ATM Company - Financial Services
Creative Brief
Bright & Fun-filled
Dean Holvery
Managing Director
PO Box 417 BUNBURY WA 6231
dean@tarvoquill.com.au
www.tarvoquill.com.au
deanh7 deanh7
Thanks for the entries so far. #1 - #35 - I need a 2 sided card, these are all only 1 side.. #36 - not too bad, dont really like the design of the black side.

```html
<!DOCTYPE html>
<html lang="en">
<head>
<meta charset="utf-8">
<title>Tarvoquill – Business Card</title>
<link rel="stylesheet" href="https://fonts.googleapis.com/css2?family=Nunito:ital,wght@0,400;0,600;0,800;1,700&display=swap">
<style>
  :root {
    --stage: #3b3b3d;
    --card-white: #ffffff;
    --brand-pink: #e6336f;
    --brand-pink-dark: #c91f58;
    --ink: #555558;
    --ink-soft: #7a7a7e;
    --rule: #c9c9cc;
    --label: #f2f2f2;
  }
  * { margin: 0; padding: 0; box-sizing: border-box; }
  html, body { width: 1200px; height: 778px; overflow: hidden; }
  body {
    background: var(--stage);
    font-family: "Nunito", Arial, sans-serif;
    position: relative;
  }
  .header-mark {
    position: absolute; top: 52px; right: 70px;
    display: flex; align-items: center; gap: 12px;
  }
  .header-mark .square { width: 26px; height: 26px; background: var(--brand-pink); border-radius: 5px; }
  .header-mark .name { color: #ffffff; font-weight: 800; font-size: 34px; letter-spacing: -0.5px; }

  .side-label {
    position: absolute; color: var(--label);
    font-style: italic; font-weight: 700; font-size: 18px;
  }
  .side-label.front { left: 70px; top: 188px; }
  .side-label.back { left: 630px; top: 188px; }

  .card {
    position: absolute; top: 222px;
    width: 500px; height: 290px; border-radius: 22px;
    box-shadow: 0 10px 24px rgba(0,0,0,.35);
    overflow: hidden;
  }
  .card-front { left: 70px; background: var(--card-white); }
  .card-back {
    left: 630px;
    background: linear-gradient(160deg, #ee4a80 0%, var(--brand-pink) 55%, var(--brand-pink-dark) 100%);
    display: flex; align-items: center; justify-content: center;
  }

  .brand { display: flex; align-items: center; gap: 14px; }
  .brand .square { border-radius: 7px; }
  .brand .name { font-weight: 800; letter-spacing: -1px; line-height: 1; }

  .card-front .brand { position: absolute; left: 34px; top: 46px; }
  .card-front .brand .square { width: 40px; height: 40px; background: var(--brand-pink); }
  .card-front .brand .name { font-size: 50px; color: var(--ink); }

  .card-back .brand .square { width: 42px; height: 42px; background: #ffffff; }
  .card-back .brand .name { font-size: 52px; color: #ffffff; }

  .holder { position: absolute; left: 36px; top: 196px; }
  .holder .person { font-size: 17px; color: var(--ink); font-weight: 600; }
  .holder .role { font-size: 11px; color: var(--brand-pink); margin-top: 1px; }

  .contact {
    position: absolute; left: 272px; top: 142px;
    border-left: 1px solid var(--rule);
    padding-left: 10px;
    font-size: 11px; color: var(--ink-soft); line-height: 1.35;
  }
  .contact .address { margin-bottom: 16px; }
  .contact ul { list-style: none; }
  .contact li { display: flex; align-items: center; gap: 6px; height: 15px; white-space: nowrap; }
  .contact svg { width: 10px; height: 10px; flex: none; }
</style>
</head>
<body>
  <div class="header-mark">
    <span class="square"></span>
    <span class="name">tarvoquill</span>
  </div>

  <p class="side-label front">Front</p>
  <p class="side-label back">Back</p>

  <section class="card card-front">
    <div class="brand">
      <span class="square"></span>
      <span class="name">tarvoquill</span>
    </div>

    <div class="holder">
      <p class="person">Dean Holvery</p>
      <p class="role">Managing Director</p>
    </div>

    <div class="contact">
      <p class="address">PO Box 417<br>TALLOWRIDGE WA 6348</p>
      <ul>
        <li>
          <svg viewBox="0 0 10 10"><rect width="10" height="10" rx="2" fill="var(--brand-pink)"/><path d="M3 2.5c.6 2.2 2.3 4 4.5 4.6l.6-1-1.3-.7-.6.6C5.3 5.6 4.5 4.8 4.1 3.9l.6-.6L4 2z" fill="#fff"/></svg>
          1300 482 617
        </li>
        <li>
          <svg viewBox="0 0 10 10"><rect width="10" height="10" rx="2" fill="var(--brand-pink)"/><rect x="3.3" y="1.8" width="3.4" height="6.4" rx=".6" fill="#fff"/></svg>
          0427 309 518
        </li>
        <li>
          <svg viewBox="0 0 10 10"><rect width="10" height="10" rx="2" fill="var(--brand-pink)"/><rect x="2" y="3" width="6" height="4" fill="#fff"/><path d="M2 3l3 2.3L8 3" stroke="var(--brand-pink)" stroke-width=".7" fill="none"/></svg>
          dean@tarvoquill.com.au
        </li>
        <li>
          <svg viewBox="0 0 10 10"><circle cx="5" cy="5" r="5" fill="var(--brand-pink)"/><circle cx="5" cy="5" r="2.8" stroke="#fff" stroke-width=".8" fill="none"/><path d="M2.2 5h5.6" stroke="#fff" stroke-width=".7"/></svg>
          www.tarvoquill.com.au
        </li>
      </ul>
    </div>
  </section>

  <section class="card card-back">
    <div class="brand">
      <span class="square"></span>
      <span class="name">tarvoquill</span>
    </div>
  </section>
</body>
</html>
```